Military training songs recorded live with troops.

I need a graphic designer (and website builder) to create the artwork, logo and website for a new company marketing campaign under the URL www.drillmoor.com.
This website will be devoted to featuring the audio catalog I created with my father in which we recorded live during PT training with troops of the R.L. Garrison.
Ultimately, I would like the website to be the one and only distribution site for our catalog. This will be the most effectively means in addressing piracy and copyright infringement. However, this would require a website platform which supports MP3 and financial sales software.
Thus, for now, the website can establish and feature the catalog we created and provide links just to Melodrop.
Thus in addition to a website, we would need graphics for the new covers for our catalog which contains 32 products.
I have attached a MP3 file to provide insight into the military cadences we recorded and have the exclusive rights to distribute and sell.

For the representation of military service to our entire society.

One-of-a-kind military training songs recorded live with troops during PT runs & marches.

• Lordcorps

Designer to choose only greyscale colors for use in the design.

• To feature the entire catalog by creating artwork for every product (cover art needed for 32 products) and separating the products under the various Armed Force: The R.L. Harbor Legion, the Army, the Air Force and the Navy. Every product must have a link for purchase from Melodrop.
• The ability to play MP3 files.
• N/A

```html
<!DOCTYPE html>
<html lang="en">
<head>
<meta charset="utf-8">
<title>Drillmoor — The Sound of Discipline</title>
<link rel="stylesheet" href="https://fonts.googleapis.com/css2?family=Playfair+Display:wght@400;600;700&family=Inter:wght@400;500&family=JetBrains+Mono:wght@400;500&display=swap">
<style>
:root{
  --bg-deep:#0d0d0d;
  --bg-archive:#131313;
  --bg-legacy:#141414;
  --bg-collection:#1a1a1a;
  --ink:#ecebe6;
  --ink-soft:#c9c9c9;
  --ink-muted:#7b7b7b;
  --ink-faint:#4c4c4c;
  --accent:#8e8e8e;
  --accent-dim:#5e5e5e;
  --tag-bg:#262626;
  --line:#2a2a2a;
  --serif:'Playfair Display', Georgia, serif;
  --sans:'Inter', Arial, sans-serif;
  --mono:'JetBrains Mono', 'Courier New', monospace;
}
*{box-sizing:border-box;margin:0;padding:0}
html,body{width:1200px;height:3396px;overflow:hidden;background:var(--bg-deep);color:var(--ink)}
body{position:relative;font-family:var(--sans)}
a{color:inherit;text-decoration:none}

/* nav */
.site-nav{position:absolute;top:0;left:0;width:1200px;height:80px;z-index:5}
.brand{position:absolute;left:69px;top:24px;font-family:var(--serif);font-size:27px;color:#9a9a9a;letter-spacing:-.5px}
.nav-links{position:absolute;top:28px;left:483px;display:flex;gap:45px;font-size:13px;letter-spacing:1.2px;color:#6e6e6e}
.nav-links .active{color:var(--ink-soft);padding-bottom:6px;border-bottom:1px solid var(--ink-soft)}
.account{position:absolute;right:68px;top:27px}

/* hero */
.hero{position:absolute;top:0;left:0;width:1200px;height:1042px;overflow:hidden;
  background:radial-gradient(ellipse at 50% 30%,#2a2a2a 0%,#1c1c1c 45%,#141414 100%)}
.hero-photo{position:absolute;left:0;top:560px;width:1200px;height:482px;
  background:linear-gradient(180deg,rgba(20,20,20,0) 0%,#262626 20%,#1e1e1e 55%,#101010 100%)}
.hero-title{position:absolute;top:240px;width:1200px;text-align:center;font-family:var(--serif);font-weight:700;font-size:70px;line-height:75px;letter-spacing:-1px;color:var(--ink)}
.hero-title .accent{color:var(--accent)}
.hero-sub{position:absolute;top:414px;width:1200px;text-align:center;font-family:var(--mono);font-size:11px;letter-spacing:1.5px;color:var(--ink-soft)}
.btn-play{position:absolute;left:524px;top:464px;width:153px;height:41px;border-radius:21px;background:var(--ink);color:#111;font-family:var(--mono);font-size:11px;letter-spacing:1.5px;display:flex;align-items:center;justify-content:center}
.play-disc{position:absolute;left:549px;top:552px;width:102px;height:102px;border-radius:50%;background:#1a1a1a;border:1px solid #333;display:flex;align-items:center;justify-content:center}
.player{position:absolute;left:241px;top:702px;width:717px;height:165px;border:1px solid rgba(255,255,255,.06);border-radius:6px;background:rgba(30,30,30,.35)}
.time{position:absolute;top:114px;font-family:var(--mono);font-size:10px;letter-spacing:1px}
.time.now{left:37px;color:var(--accent)}
.time.total{right:37px;color:var(--ink-muted)}
.track{position:absolute;left:29px;top:138px;width:653px;height:1px;background:#333}
.track-fill{position:absolute;left:0;top:0;width:238px;height:1px;background:var(--accent)}
.track-knob{position:absolute;left:232px;top:-5px;width:11px;height:11px;border-radius:50%;background:var(--accent);border:2px solid #3a3a3a}

/* archive */
.archive{position:absolute;top:1042px;left:0;width:1200px;height:921px;background:var(--bg-archive);overflow:hidden}
.section-title{font-family:var(--serif);font-weight:700;font-size:45px;line-height:54px;color:var(--ink)}
.eyebrow{font-family:var(--mono);font-size:11px;letter-spacing:1.6px;color:var(--ink-muted)}
.archive .section-title{position:absolute;left:60px;top:122px}
.archive .eyebrow{position:absolute;left:60px;top:189px}
.force-tabs{position:absolute;left:420px;top:169px;display:flex;gap:24px;font-family:var(--mono);font-size:11px;letter-spacing:1.4px;color:var(--ink-faint)}
.force-tabs .active{color:var(--ink-soft);padding-bottom:5px;border-bottom:1px solid var(--ink-soft)}
.arrow-btn{position:absolute;top:154px;width:46px;height:46px;border-radius:50%;border:1px solid #555;display:flex;align-items:center;justify-content:center}
.record{position:absolute;top:261px;width:359px}
.record-art{width:359px;height:359px;border:1px solid #2a2a2a}
.art-boots{background:radial-gradient(ellipse at 50% 60%,#5a5a5a 0%,#333 45%,#161616 100%)}
.art-mud{background:radial-gradient(ellipse at 60% 55%,#4a4a4a 0%,#2c2c2c 50%,#1a1a1a 100%)}
.art-tags{background:radial-gradient(ellipse at 45% 50%,#555 0%,#2e2e2e 40%,#141414 100%)}
.tag{display:inline-block;margin-top:32px;padding:3px 8px;border-radius:2px;font-family:var(--mono);font-size:9px;letter-spacing:.8px;background:var(--tag-bg);color:var(--accent-dim)}
.tag.rare{background:#3a3a3a;color:#585858}
.record-meta{margin-top:8px;font-family:var(--mono);font-size:11px;letter-spacing:1.6px;color:var(--ink-faint)}
.record-title{margin-top:6px;font-family:var(--serif);font-size:30px;font-weight:400;color:var(--ink)}
.buy-link{margin-top:14px;display:inline-flex;align-items:center;gap:10px;font-family:var(--mono);font-size:10px;letter-spacing:1.5px;color:var(--ink-muted)}

/* legacy */
.legacy{position:absolute;top:1963px;left:0;width:1200px;height:803px;background:var(--bg-legacy)}
.legacy-art{position:absolute;left:61px;top:120px;width:494px;height:562px;background:radial-gradient(ellipse at 45% 55%,#4a4a4a 0%,#2a2a2a 45%,#121212 100%)}
.fragment{position:absolute;left:314px;top:470px;width:241px;height:155px;background:#232323;border:1px solid #333;padding:26px 14px 0 32px;transform:rotate(-1deg)}
.fragment-label{font-family:var(--mono);font-size:10px;letter-spacing:1px;color:var(--accent)}
.fragment-quote{margin-top:14px;font-size:12.5px;line-height:20px;color:var(--ink-soft)}
.legacy-copy{position:absolute;left:645px;top:168px;width:495px}
.legacy-label{display:flex;align-items:center;gap:14px;font-family:var(--mono);font-size:11px;letter-spacing:1.6px;color:var(--accent)}
.legacy-label::before{content:"";width:46px;height:1px;background:var(--accent)}
.legacy-copy .section-title{margin-top:28px;font-size:44px;line-height:56px}
.legacy-copy p.body{margin-top:30px;width:482px;font-size:16.5px;line-height:27.5px;color:var(--ink-soft)}
.legacy-copy p.body + p.body{margin-top:30px}
.legacy-rule{margin-top:48px;height:1px;background:var(--line)}
.origin-link{margin-top:26px;display:flex;align-items:center;gap:14px;font-family:var(--mono);font-size:11px;letter-spacing:1.6px;color:var(--ink)}

/* collection */
.collection{position:absolute;top:2766px;left:0;width:1200px;height:330px;background:var(--bg-collection)}
.collection .section-title{position:absolute;left:60px;top:95px}
.collection-stats{position:absolute;left:60px;top:218px;display:flex;gap:10px;font-family:var(--mono);font-size:11px;letter-spacing:1.4px;line-height:12px;color:var(--ink-muted)}
.collection-stats::before{content:"";width:28px;height:1px;margin-top:10px;background:#444}
.format{position:absolute;top:92px;width:148px;height:148px;display:flex;flex-direction:column;align-items:center;justify-content:center;gap:10px}
.format-type{font-family:var(--mono);font-size:9px;letter-spacing:1px;color:var(--ink-muted)}
.format-name{font-family:var(--serif);font-size:20px;color:var(--ink-soft)}
.f-cassette{left:481px;background:#222}
.f-vinyl{left:652px;background:#222;border-radius:50%}
.f-digital{left:822px;background:#222;border:1px solid #3a3a3a;border-radius:8px}
.f-box{left:992px;background:linear-gradient(180deg,#363636 0%,#282828 50%,#1e1e1e 100%)}

/* footer */
.site-footer{position:absolute;top:3096px;left:0;width:1200px;height:300px;background:var(--bg-deep)}
.site-footer .brand{left:60px;top:126px;font-size:28px;color:var(--ink)}
.footer-tagline{position:absolute;left:60px;top:168px;font-family:var(--mono);font-size:9px;letter-spacing:.8px;color:var(--ink-muted)}
.footer-links{position:absolute;left:413px;top:144px;display:flex;gap:30px;font-family:var(--mono);font-size:11px;letter-spacing:1.4px;color:var(--ink-soft)}
.copyright{position:absolute;right:61px;top:144px;font-family:var(--mono);font-size:10px;letter-spacing:1.6px;color:var(--ink-muted)}
</style>
</head>
<body>

<section class="hero">
  <div class="hero-photo" role="img" aria-label="Column of troops running through morning fog"></div>
  <h1 class="hero-title">THE SOUND OF<br><span class="accent">DISCIPLINE</span></h1>
  <p class="hero-sub">LIVE MILITARY CADENCES. RECORDED. PRESERVED. SHARED.</p>
  <a class="btn-play" href="#">PLAY ARCHIVE</a>
  <div class="play-disc">
    <svg width="24" height="26" viewBox="0 0 24 26"><path d="M3 2 L22 13 L3 24 Z" fill="#ecebe6"/></svg>
  </div>
  <div class="player">
    <span class="time now">01:24</span>
    <span class="time total">03:45</span>
    <div class="track"><div class="track-fill"></div><div class="track-knob"></div></div>
  </div>
</section>

<nav class="site-nav">
  <a class="brand" href="#">DRILLMOOR</a>
  <div class="nav-links">
    <a class="active" href="#">ARCHIVE</a>
    <a href="#">LEGACY</a>
    <a href="#">CADENCES</a>
    <a href="#">ABOUT</a>
  </div>
  <svg class="account" width="22" height="22" viewBox="0 0 22 22" fill="none" stroke="#9a9a9a" stroke-width="1.6">
    <circle cx="11" cy="11" r="9.5"/><circle cx="11" cy="9" r="3.2"/><path d="M5 17.5c1.5-2.5 3.5-3.5 6-3.5s4.5 1 6 3.5"/>
  </svg>
</nav>

<section class="archive">
  <h2 class="section-title">THE ARCHIVE</h2>
  <p class="eyebrow">RESTORED FIELD RECORDINGS</p>
  <nav class="force-tabs" aria-label="Filter by armed force">
    <a class="active" href="#">ALL</a>
    <a href="#">HARBOR LEGION</a>
    <a href="#">ARMY</a>
    <a href="#">AIR FORCE</a>
    <a href="#">NAVY</a>
  </nav>
  <a class="arrow-btn" style="left:1034px" href="#" aria-label="Previous">
    <svg width="16" height="14" viewBox="0 0 16 14" fill="none" stroke="#ecebe6" stroke-width="1.6"><path d="M15 7H2M7 1L1 7l6 6"/></svg>
  </a>
  <a class="arrow-btn" style="left:1094px" href="#" aria-label="Next">
    <svg width="16" height="14" viewBox="0 0 16 14" fill="none" stroke="#ecebe6" stroke-width="1.6"><path d="M1 7h13M9 1l6 6-6 6"/></svg>
  </a>

  <article class="record" style="left:60px">
    <div class="record-art art-boots" role="img" aria-label="Worn combat boots on gravel"></div>
    <span class="tag">RESTORED AUDIO</span>
    <p class="record-meta">1987 · 7TH INFANTRY</p>
    <h3 class="record-title">Morning Run</h3>
    <a class="buy-link" href="#">BUY ON MELODROP
      <svg width="14" height="10" viewBox="0 0 14 10" fill="none" stroke="#7b7b7b" stroke-width="1.4"><path d="M1 5h11M8 1l4 4-4 4"/></svg></a>
  </article>
  <article class="record" style="left:451px">
    <div class="record-art art-mud" role="img" aria-label="Muddy laced boots on wet ground"></div>
    <span class="tag rare">RARE RECORD</span>
    <p class="record-meta">1968 · AIRBORNE</p>
    <h3 class="record-title">Night Jump</h3>
    <a class="buy-link" href="#">BUY ON MELODROP
      <svg width="14" height="10" viewBox="0 0 14 10" fill="none" stroke="#7b7b7b" stroke-width="1.4"><path d="M1 5h11M8 1l4 4-4 4"/></svg></a>
  </article>
  <article class="record" style="left:841px">
    <div class="record-art art-tags" role="img" aria-label="Close-up of identification tags on fabric"></div>
    <span class="tag">REMASTERED</span>
    <p class="record-meta">1992 · HARBOR LEGION</p>
    <h3 class="record-title">The Grinder</h3>
    <a class="buy-link" href="#">BUY ON MELODROP
      <svg width="14" height="10" viewBox="0 0 14 10" fill="none" stroke="#7b7b7b" stroke-width="1.4"><path d="M1 5h11M8 1l4 4-4 4"/></svg></a>
  </article>
</section>

<section class="legacy">
  <div class="legacy-art" role="img" aria-label="Vintage field tape recorder in a dim barracks room"></div>
  <div class="fragment">
    <p class="fragment-label">ARCHIVE FRAGMENT · 1987</p>
    <p class="fragment-quote">"...the cadence isn't just rhythm. It's the collective breath of fifty men moving as one."</p>
  </div>
  <div class="legacy-copy">
    <p class="legacy-label">THE LEGACY</p>
    <h2 class="section-title">PRESERVING THE<br>ECHOES OF DUTY</h2>
    <p class="body">These recordings were never intended to become products. They began as a way to preserve moments of effort, rhythm, and shared endurance. Today, they remain exactly as they were captured.</p>
    <p class="body">They are raw, visceral audio documents captured on the march, representing the sound of discipline and endurance.</p>
    <div class="legacy-rule"></div>
    <a class="origin-link" href="#">READ THE ORIGIN STORY
      <svg width="16" height="12" viewBox="0 0 16 12" fill="none" stroke="#ecebe6" stroke-width="1.6"><path d="M1 6h13M9 1l5 5-5 5"/></svg>
    </a>
  </div>
</section>

<section class="collection">
  <h2 class="section-title">THE<br>COLLECTION</h2>
  <p class="collection-stats"><span>32 recordings | 9 hours preserved |<br>1987–1998</span></p>
  <div class="format f-cassette"><span class="format-type">TYPE 01</span><span class="format-name">Cassette</span></div>
  <div class="format f-vinyl"><span class="format-type">TYPE 02</span><span class="format-name">Vinyl</span></div>
  <div class="format f-digital"><span class="format-type">TYPE 03</span><span class="format-name">Digital</span></div>
  <div class="format f-box" role="img" aria-label="Stacked archive tape boxes"><span class="format-type">TYPE 04</span><span class="format-name">Archive Box</span></div>
</section>

<footer class="site-footer">
  <a class="brand" href="#">DRILLMOOR</a>
  <p class="footer-tagline">Preserving the rhythm of endurance.</p>
  <div class="footer-links"><a href="#">TERMS</a><a href="#">PRIVACY</a><a href="#">CONTACT</a></div>
  <p class="copyright">© 2026 DRILLMOOR ARCHIVE. ALL RIGHTS RESERVED.</p>
</footer>

</body>
</html>
```